Business Card for Managing Partner Investment Fund

To create a business card template for an investment fund manager. Business card should be more professional in nature, not too colorful, more upscale, and created using the attached logos and fund name files. I would prefer a black or gray color scheme, but am open to the use of color as well. I would prefer a double sided business card, but open to single sided business card designs as well. The business card should include: name, title, and contact information, as well as logo and company name. I would prefer a more stream-lined, simple business card design.
Updates
Address: 4136 NE 19th Ter. Ocala, FL 34470
Email: travis48@quillnet-mail.com
Phone: 561-374-9186
Title: managing partner
Name: Travis Whitlow
Fund Name: Emberfall Capital
Logos can be found in files attached to the brief
Target Market(s)
potential investors, other fund managers
Industry/Entity Type
Finance
Contact Information for Business Card
Name on card: Travis Whitlow
Title: Managing Partner
Font styles to use
Colors
Designer to choose colors to be used in the design.
Requirements
Must have
- Phone number
- email address
- physical address
- title
- name
- logo
- Fund name
Nice to have
- simple layout
Should not have
- too many colors, busy fonts,

```html
<!DOCTYPE html>
<html lang="en">
<head>
<meta charset="utf-8">
<title>Emberfall Capital – Business Card</title>
<link href="https://fonts.googleapis.com/css2?family=Tinos:wght@400&display=swap" rel="stylesheet">
<style>
  :root {
    --backdrop: #3b3b3d;
    --card: #1c1c1d;
    --card-edge: #2a2a2b;
    --ink: #b9b9bb;
    --ink-soft: #8e8e91;
    --rule: #5a5a5d;
  }
  * { margin: 0; padding: 0; box-sizing: border-box; }
  html, body {
    width: 1200px;
    height: 671px;
    overflow: hidden;
    background: var(--backdrop);
    font-family: "Tinos", "Times New Roman", serif;
    color: var(--ink);
  }
  .sheet {
    width: 1200px;
    height: 671px;
    display: flex;
    align-items: center;
    justify-content: center;
    gap: 40px;
  }
  .card {
    position: relative;
    width: 520px;
    height: 297px;
    background: linear-gradient(160deg, var(--card-edge) 0%, var(--card) 60%);
    border-radius: 3px;
    box-shadow: 0 14px 30px rgba(0, 0, 0, 0.45);
  }

  /* Front */
  .card--front {
    display: flex;
    align-items: center;
    justify-content: center;
  }
  .wordmark {
    color: var(--ink);
    font-weight: 400;
    text-transform: uppercase;
    line-height: 1;
    text-align: center;
    white-space: nowrap;
  }
  .wordmark__main { display: block; letter-spacing: 0.06em; }
  .wordmark__sub { display: block; letter-spacing: 0.3em; margin-left: 0.3em; }
  .wordmark--large .wordmark__main { font-size: 46px; }
  .wordmark--large .wordmark__sub { font-size: 22px; margin-top: 8px; }
  .wordmark--small .wordmark__main { font-size: 22px; }
  .wordmark--small .wordmark__sub { font-size: 11px; margin-top: 4px; }

  /* Back */
  .card--back .wordmark--small {
    position: absolute;
    left: 40px;
    top: 36px;
  }
  .holder {
    position: absolute;
    left: 40px;
    top: 128px;
  }
  .holder__name {
    font-size: 17px;
    letter-spacing: 0.04em;
    text-transform: uppercase;
    color: var(--ink);
  }
  .holder__title {
    margin-top: 4px;
    font-size: 8px;
    letter-spacing: 0.12em;
    text-transform: uppercase;
    color: var(--ink-soft);
  }
  .contact {
    position: absolute;
    display: flex;
    gap: 14px;
    font-size: 12px;
    line-height: 1.4;
    color: var(--ink-soft);
    letter-spacing: 0.02em;
  }
  .contact svg {
    width: 12px;
    height: 12px;
    flex: none;
    margin-top: 2px;
    fill: var(--ink-soft);
  }
  .contact--phone { left: 40px; top: 186px; }
  .contact--web { left: 300px; top: 158px; }
  .contact--address { left: 300px; top: 206px; }
  .divider {
    position: absolute;
    left: 272px;
    top: 150px;
    width: 1px;
    height: 92px;
    background: var(--rule);
  }
</style>
</head>
<body>
<main class="sheet">

  <section class="card card--front" aria-label="Card front">
    <p class="wordmark wordmark--large">
      <span class="wordmark__main">Emberfall</span>
      <span class="wordmark__sub">Capital</span>
    </p>
  </section>

  <section class="card card--back" aria-label="Card back">
    <p class="wordmark wordmark--small">
      <span class="wordmark__main">Emberfall</span>
      <span class="wordmark__sub">Capital</span>
    </p>

    <div class="holder">
      <p class="holder__name">Travis Whitlow</p>
      <p class="holder__title">Managing Partner</p>
    </div>

    <div class="contact contact--phone">
      <svg viewBox="0 0 24 24" aria-hidden="true"><path d="M6.6 10.8a15.1 15.1 0 0 0 6.6 6.6l2.2-2.2c.3-.3.7-.4 1-.2 1.1.4 2.3.6 3.6.6.6 0 1 .4 1 1V20c0 .6-.4 1-1 1A17 17 0 0 1 3 4c0-.6.4-1 1-1h3.5c.6 0 1 .4 1 1 0 1.3.2 2.5.6 3.6.1.3 0 .7-.2 1z"/></svg>
      <div>
        <p>555-0142</p>
        <p>555-0143</p>
      </div>
    </div>

    <span class="divider" aria-hidden="true"></span>

    <div class="contact contact--web">
      <svg viewBox="0 0 24 24" aria-hidden="true"><path d="M12 2a10 10 0 1 0 0 20 10 10 0 0 0 0-20zm6.9 6h-2.9a15.7 15.7 0 0 0-1.4-3.6A8 8 0 0 1 18.9 8zM12 4c.8 1.2 1.5 2.5 1.9 4h-3.8c.4-1.5 1.1-2.8 1.9-4zM4.3 14a8.2 8.2 0 0 1 0-4h3.4a16.5 16.5 0 0 0 0 4zm.8 2h2.9c.3 1.3.8 2.5 1.4 3.6A8 8 0 0 1 5.1 16zM8 8H5.1a8 8 0 0 1 4.3-3.6C8.8 5.5 8.3 6.7 8 8zm4 12c-.8-1.2-1.5-2.5-1.9-4h3.8c-.4 1.5-1.1 2.8-1.9 4zm2.3-6H9.7a14.7 14.7 0 0 1 0-4h4.6a14.7 14.7 0 0 1 0 4zm.3 5.6c.6-1.1 1.1-2.3 1.4-3.6h2.9a8 8 0 0 1-4.3 3.6zm1.7-5.6a16.5 16.5 0 0 0 0-4h3.4a8.2 8.2 0 0 1 0 4z"/></svg>
      <div>
        <p>travis@example.com</p>
        <p>www.example.com</p>
      </div>
    </div>

    <div class="contact contact--address">
      <svg viewBox="0 0 24 24" aria-hidden="true"><path d="M12 2a7 7 0 0 0-7 7c0 5.3 7 13 7 13s7-7.7 7-13a7 7 0 0 0-7-7zm0 9.5a2.5 2.5 0 1 1 0-5 2.5 2.5 0 0 1 0 5z"/></svg>
      <div>
        <p>100 Sample Lane</p>
        <p>Fernhollow 00000</p>
      </div>
    </div>
  </section>

</main>
</body>
</html>
```